Designer Instructions – Updated Referral Program Flyer

(Based on the mock-up in “Brief Layout and Instructions.pdf”)

OVERALL STYLE + LAYOUT

Maintain the same general layout, structure, and flow as the mock-up flyer (front and back).

This is an update of an older flyer, not a full redesign — keep the same sections, proportions, and overall visual feel, but with cleaner, more modern design improvements.

The final flyer should look clean, bold, professional, and high-impact, geared toward realtors, property managers, and contractors who refer work.

FRONT SIDE INSTRUCTIONS
1. Header Section

Remove the Tallow Ridge Builders logo from the top banner.
(Shown on page 1 of the PDF)

2. Main Headline

Keep the same three-line structure:
EARN
UNLIMITED
CASH

Center it, maximize impact, and increase the font size of CASH so all three words match in importance.

Make the headline bold, clean, and the main focal point.

3. Cash Incentive Box

Keep the "$500 minimum OR 10% per referral" box, but upgrade the graphics to look sharper and more modern.

Ensure the wording matches exactly what’s in the mock-up.

4. Premier Partner Program Ribbon

Clean up and modernize the "PREMIER PARTNER PROGRAM" bar while keeping the same position and structure.

Ensure the checkmark badge remains crisp and professional.

5. Supporting Icons Section

Keep the four icons/benefit boxes (Guaranteed Payout, Free Evaluations, Affordable Solutions, Industry Leaders) in the same order.

Update the icons to cleaner, more modern styles — but maintain the same meanings.

Improve alignment and spacing for sharper visual consistency.

6. Remove Icons in Contact Area

At the bottom (“CALL TEXT OR BOOK ONLINE 555-014-2796 TallowRidgeBuilders.example”), remove the phone and internet icons, as noted on page 2 of the PDF.

7. Replace All Images

I (Darnell) will provide all updated stock images separately via email.

Replace the flood/water-damage imagery and roof leak with the new images I send.

Keep image placement and proportions the same as the mock-up.

BACK SIDE INSTRUCTIONS
1. Header Image + “REFER / EARN” Section

Maintain the same large split-image layout (“The more you refer, the more you earn”).

Replace all background imagery with the new assets I will send.

Keep the CASH FLOW image section but modernize the type and spacing.

2. “HOW IT WORKS” Section

Preserve the three-column layout:

Refer Flood, Water & Mold Damage

We Take Care of Everything (evaluations/insurance)

Get Paid to Share

Update images, tighten spacing, and use modern iconography.

3. Remove Phone/Internet Icons

Same as the front side — remove small communication icons and keep only the text/number/URL.

4. Bottom Contact Bar

Keep the blue bar, same wording, same layout — just modernize the style if needed for clarity.

5. Replace All Back-Side Images

Again, I will email you the image assets.

Keep the layout EXACT — just update with higher-quality photos and improved design.

TEXT CONTENT (Keep as-is unless spacing adjustments needed)

All text shown in the PDF should remain exactly the same unless spacing or visual balance requires minor adjustments.
Example from page 3:

“REFER FLOOD, MOLD & CONSTRUCTION JOBS”

“We Schedule a Free Estimate. If Approved, You Get Paid.”

“Everybody Benefits From Referrals”

Everything stays, just refreshed and visually improved.

DESIGN GOALS

Flyer should look high-end and trustworthy, not salesy.

Consistent color theme: blues, whites, yellows, same palette as original.

Use bold, modern fonts with strong readability.

Ensure all headlines pop and all benefit boxes are clean, well-aligned, and evenly spaced.

The final result should feel like a premium referral program flyer for a top-tier restoration/remodel company.

FILES I WILL PROVIDE

I will send the designer:

All replacement stock photos

Any updated logos (if needed)

Original high-resolution version of the mock-up (if available)

Any additional icons preferred

0054AA
0677BA
7BADD7
CADEEF
E8F1F8

• Designer Instructions – Updated Referral Program Flyer (Based on the mock-up in “Brief Layout and Instructions.pdf”) OVERALL STYLE + LAYOUT Maintain the same general layout, structure, and flow as the mock-up flyer (front and back). This is an update of an older flyer, not a full redesign — keep the same sections, proportions, and overall visual feel, but with cleaner, more modern design improvements. The final flyer should look clean, bold, professional, and high-impact, geared toward realtors, property managers, and contractors who refer work. FRONT SIDE INSTRUCTIONS 1. Header Section Remove the Tallow Ridge Builders logo from the top banner. (Shown on page 1 of the PDF) 2. Main Headline Keep the same three-line structure: EARN UNLIMITED CASH Center it, maximize impact, and increase the font size of CASH so all three words match in importance. Make the headline bold, clean, and the main focal point. 3. Cash Incentive Box Keep the "$500 minimum OR 10% per referral" box, but upgrade the graphics to look sharper and more modern. Ensure the wording matches exactly what’s in the mock-up. 4. Premier Partner Program Ribbon Clean up and modernize the "PREMIER PARTNER PROGRAM" bar while keeping the same position and structure. Ensure the checkmark badge remains crisp and professional. 5. Supporting Icons Section Keep the four icons/benefit boxes (Guaranteed Payout, Free Evaluations, Affordable Solutions, Industry Leaders) in the same order. Update the icons to cleaner, more modern styles — but maintain the same meanings. Improve alignment and spacing for sharper visual consistency. 6. Remove Icons in Contact Area At the bottom (“CALL TEXT OR BOOK ONLINE 555-014-2796 TallowRidgeBuilders.example”), remove the phone and internet icons, as noted on page 2 of the PDF. 7. Replace All Images I (Darnell) will provide all updated stock images separately via email. Replace the flood/water-damage imagery and roof leak with the new images I send. Keep image placement and proportions the same as the mock-up. BACK SIDE INSTRUCTIONS 1. Header Image + “REFER / EARN” Section Maintain the same large split-image layout (“The more you refer, the more you earn”). Replace all background imagery with the new assets I will send. Keep the CASH FLOW image section but modernize the type and spacing. 2. “HOW IT WORKS” Section Preserve the three-column layout: Refer Flood, Water & Mold Damage We Take Care of Everything (evaluations/insurance) Get Paid to Share Update images, tighten spacing, and use modern iconography. 3. Remove Phone/Internet Icons Same as the front side — remove small communication icons and keep only the text/number/URL. 4. Bottom Contact Bar Keep the blue bar, same wording, same layout — just modernize the style if needed for clarity. 5. Replace All Back-Side Images Again, I will email you the image assets. Keep the layout EXACT — just update with higher-quality photos and improved design. TEXT CONTENT (Keep as-is unless spacing adjustments needed) All text shown in the PDF should remain exactly the same unless spacing or visual balance requires minor adjustments. Example from page 3: “REFER FLOOD, MOLD & CONSTRUCTION JOBS” “We Schedule a Free Estimate. If Approved, You Get Paid.” “Everybody Benefits From Referrals” Everything stays, just refreshed and visually improved. DESIGN GOALS Flyer should look high-end and trustworthy, not salesy. Consistent color theme: blues, whites, yellows, same palette as original. Use bold, modern fonts with strong readability. Ensure all headlines pop and all benefit boxes are clean, well-aligned, and evenly spaced. The final result should feel like a premium referral program flyer for a top-tier restoration/remodel company. FILES I WILL PROVIDE I will send the designer: All replacement stock photos Any updated logos (if needed) Original high-resolution version of the mock-up (if available) Any additional icons preferred

```html
<!DOCTYPE html>
<html lang="en">
<head>
<meta charset="utf-8">
<title>Referral Program Flyer – Front and Back</title>
<link href="https://fonts.googleapis.com/css2?family=Anton&family=Montserrat:wght@500;700;800;900&family=Poppins:wght@300;400;500&display=swap" rel="stylesheet">
<style>
  :root{
    --navy:#0c2d6b;
    --navy-deep:#0a1a3a;
    --red:#e1333a;
    --yellow:#f8d81a;
    --ink:#161616;
    --text:#2b2b2b;
    --paper:#ffffff;
    --stage:#d9d9d9;
    --rule:#8c9bb3;
  }
  *{box-sizing:border-box;margin:0;padding:0}
  html,body{width:897px;height:1200px;overflow:hidden;background:var(--stage)}
  body{position:relative;font-family:"Poppins",sans-serif;color:var(--text)}
  .flyer{position:absolute;left:89px;width:719px;height:465px;background:var(--paper);overflow:hidden;box-shadow:0 2px 8px rgba(0,0,0,.18)}
  .flyer--front{top:94px}
  .flyer--back{top:640px}
  .flyer__art{position:absolute;inset:0;width:719px;height:465px}
  .abs{position:absolute}

  .hl-red{font-family:"Montserrat",sans-serif;font-weight:900;fill:var(--red)}
  .hl-navy{font-family:"Montserrat",sans-serif;font-weight:900;fill:var(--navy)}
  .hl-white{font-family:"Montserrat",sans-serif;font-weight:900;fill:#fff}
  .hl-condensed{font-family:"Anton",sans-serif}

  .offer{left:24px;top:236px;display:flex;align-items:center;gap:3px;font-family:"Montserrat",sans-serif}
  .offer__amount{font-weight:900;font-size:30px;color:var(--navy);letter-spacing:-1px;line-height:1}
  .offer__amount sup{font-size:15px;vertical-align:12px;margin-right:1px}
  .offer__pill{background:var(--red);color:#fff;font-weight:700;font-size:12px;padding:1px 10px;border-radius:10px;margin-left:-2px}
  .offer__or{width:22px;height:22px;border-radius:50%;background:var(--yellow);border:2px solid #fff;box-shadow:0 0 0 1px #d9b400;color:var(--navy);font-size:8px;font-weight:900;display:flex;align-items:center;justify-content:center;margin:0 4px}

  .ribbon{left:378px;top:242px;display:flex;align-items:center;gap:6px;font-family:"Montserrat",sans-serif;color:var(--navy)}
  .ribbon__lead{font-size:8.5px;font-weight:700;letter-spacing:5px}
  .ribbon__word{font-size:18px;font-weight:800}
  .ribbon__or{width:19px;height:19px;border-radius:50%;background:var(--red);border:2px solid #fff;box-shadow:0 0 0 1px var(--red);color:#fff;font-size:7px;font-weight:900;display:flex;align-items:center;justify-content:center}

  .wins{left:0;width:719px;top:282px;text-align:center;font-family:"Montserrat",sans-serif;font-weight:800;font-size:17.5px;color:var(--navy)}

  .benefit{position:absolute;top:316px;width:152px}
  .benefit__pill{display:flex;align-items:center;height:16px;margin-top:5px;border-radius:8px;color:#fff;font-family:"Montserrat",sans-serif;font-weight:700;font-size:8.5px;padding-left:32px}
  .benefit__icon{position:absolute;left:0;top:0;width:27px;height:27px;border-radius:50%;background:#fff;border:1px solid #c9d0dc;display:flex;align-items:center;justify-content:center}
  .benefit--red .benefit__pill{background:var(--red)}
  .benefit--navy .benefit__pill{background:var(--navy)}
  .benefit__stem{position:absolute;left:50%;top:21px;width:1px;height:10px;background:var(--rule)}
  .benefit__stem::after{content:"";position:absolute;left:-1.5px;bottom:-2px;width:4px;height:4px;border-radius:50%;background:currentColor}
  .benefit--red .benefit__stem{color:var(--red)}
  .benefit--navy .benefit__stem{color:var(--navy)}
  .benefit__text{position:absolute;top:38px;left:-10px;right:-10px;text-align:center;font-size:8.4px;font-weight:300;line-height:11.5px;color:var(--ink)}

  .steps{left:29px;top:389px;display:flex;align-items:center;font-family:"Montserrat",sans-serif;font-weight:800;font-size:17px;color:var(--ink);gap:20px}
  .steps span,.refer-row span{display:flex;align-items:center;gap:7px}
  .tick{width:12px;height:12px;flex:none}

  .cta__label{font-family:"Montserrat",sans-serif;font-weight:700;color:#fff;font-size:15.5px}
  .cta__contact{font-family:"Poppins",sans-serif;font-weight:400;color:var(--ink);display:flex;gap:8px;align-items:center;white-space:nowrap}
  .cta__contact i{display:block;width:1px;height:16px;background:#777}

  .badge{left:620px;top:392px;width:66px;height:66px;border-radius:50%;background:#fff;border:3px solid var(--red);display:flex;flex-direction:column;align-items:center;justify-content:center;font-family:"Montserrat",sans-serif;color:var(--red);line-height:1}
  .badge__num{font-size:26px;font-weight:900;font-style:normal}
  .badge__unit{font-size:8px;font-weight:800;background:var(--red);color:#fff;padding:1px 5px;border-radius:6px;margin-top:2px}

  .how{left:29px;top:277px;font-family:"Montserrat",sans-serif;font-weight:800;font-size:22.5px;color:var(--navy);letter-spacing:-.5px;white-space:nowrap}
  .how-rule{left:237px;top:291px;width:448px;height:1px;background:#b9c1cc}
  .step-photo{position:absolute;top:317px;width:93px;height:56px;border:1px solid #9fb4d4}
  .step-copy{position:absolute;top:318px;width:120px}
  .step-copy h3{font-family:"Montserrat",sans-serif;font-weight:800;font-size:9.6px;line-height:10.5px;color:var(--red)}
  .step-copy p{font-size:8.8px;line-height:11px;color:var(--ink);margin-top:2px}

  .refer-row{left:29px;top:388px;display:flex;align-items:center;font-family:"Montserrat",sans-serif;font-weight:800;font-size:17px;color:var(--ink)}
  .refer-row__pill{background:var(--navy);color:#fff;border-radius:12px;height:22px;width:92px;display:flex;align-items:center;justify-content:center;font-size:18px;margin-right:14px}
  .refer-row__sep{width:1px;height:22px;background:#999;margin:0 16px}
</style>
</head>
<body>

<section class="flyer flyer--front" aria-label="Referral program flyer front">
  <svg class="flyer__art" viewBox="0 0 719 465" xmlns="http://www.w3.org/2000/svg">
    <defs>
      <linearGradient id="roomTone" x1="0" y1="0" x2="0.4" y2="1">
        <stop offset="0" stop-color="#d9d6cf"/>
        <stop offset="0.45" stop-color="#b79d7f"/>
        <stop offset="1" stop-color="#7a5334"/>
      </linearGradient>
    </defs>
    <polygon points="396,0 719,0 719,235 306,235" fill="url(#roomTone)" role="img" aria-label="Photo of a flood-damaged living room with the floor opened to the joists"/>
    <polygon points="385,0 396,0 306,235 295,235" fill="var(--yellow)"/>
    <polygon points="0,69 257,69 281,114 0,114" fill="var(--yellow)"/>
    <polygon points="0,114 283,114 327,191 0,191" fill="var(--navy)"/>
    <polygon points="0,191 351,191 351,227 0,227" fill="var(--yellow)"/>
    <polygon points="0,227 356,227 352,235 0,235" fill="var(--navy)"/>
    <polygon points="359,238 719,238 719,269 372,269" fill="var(--yellow)"/>

    <text class="hl-red" x="29" y="60" font-size="58" textLength="171" lengthAdjust="spacingAndGlyphs">EARN</text>
    <text class="hl-navy" x="29" y="108" font-size="42" textLength="220" lengthAdjust="spacingAndGlyphs">UNLIMITED</text>
    <text class="hl-white" x="29" y="174" font-size="62" textLength="169" lengthAdjust="spacingAndGlyphs">CA$H</text>
    <text class="hl-navy" x="25" y="217" font-size="21" textLength="310" lengthAdjust="spacingAndGlyphs">GET PAID TOREFER A FLOOD</text>

    <path d="M29,308 V294 H156 M561,294 H689 V308" fill="none" stroke="var(--rule)" stroke-width="1"/>

    <polygon points="0,422 271,422 277,436 271,449 0,449" fill="var(--red)"/>
    <polygon points="0,449 719,449 719,465 0,465" fill="var(--navy)"/>
  </svg>

  <div class="abs offer">
    <span class="offer__amount"><sup>$</sup>500</span>
    <span class="offer__pill">Minimum</span>
    <span class="offer__or">OR</span>
    <span class="offer__amount">10%</span>
    <span class="offer__pill">Minimum</span>
  </div>

  <div class="abs ribbon">
    <span class="ribbon__lead">PREMIER</span>
    <span class="ribbon__word">PARTNER</span>
    <span class="ribbon__or">OR</span>
    <span class="ribbon__word">PROGRAM</span>
  </div>

  <h2 class="abs wins">PARTNER WITH US &amp; EVERYBODY WINS!</h2>

  <div class="benefit benefit--red" style="left:29px">
    <div class="benefit__pill">GUARANTEED PAYOUT</div>
    <span class="benefit__icon"><svg width="14" height="14" viewBox="0 0 14 14"><circle cx="7" cy="6" r="5" fill="var(--navy)"/><path d="M4.6 6l1.6 1.6L9.4 4.4" stroke="#fff" stroke-width="1.4" fill="none"/></svg></span>
    <span class="benefit__stem"></span>
    <p class="benefit__text">Minimum $500 or 10% of<br>Total Invoice Paid Fast</p>
  </div>
  <div class="benefit benefit--navy" style="left:197px">
    <div class="benefit__pill">FREE ESTIMATES</div>
    <span class="benefit__icon"><svg width="14" height="14" viewBox="0 0 14 14"><rect x="3" y="1.5" width="8" height="11" rx="1" fill="none" stroke="var(--navy)" stroke-width="1.3"/><path d="M5 5h4M5 7.5h4M5 10h2.5" stroke="var(--navy)" stroke-width="1.1"/></svg></span>
    <span class="benefit__stem"></span>
    <p class="benefit__text">Fast &amp; Free Inspections &amp;<br>Written Estimates</p>
  </div>
  <div class="benefit benefit--red" style="left:364px;width:158px">
    <div class="benefit__pill">AFFORDABLE SOLUTIONS</div>
    <span class="benefit__icon"><svg width="14" height="14" viewBox="0 0 14 14"><circle cx="7" cy="6" r="4.5" fill="none" stroke="var(--navy)" stroke-width="1.3"/><path d="M7 3.6v4.8M5.7 4.8h2.2a.9.9 0 010 1.8H6.1a.9.9 0 000 1.8h2.2" stroke="var(--navy)" stroke-width="1" fill="none"/><path d="M3 12.5h8" stroke="var(--red)" stroke-width="1.3"/></svg></span>
    <span class="benefit__stem"></span>
    <p class="benefit__text">Lowest Out of Pocket<br>Costs for Your Customers</p>
  </div>
  <div class="benefit benefit--navy" style="left:536px">
    <div class="benefit__pill">INDUSTRY LEADERS</div>
    <span class="benefit__icon"><svg width="14" height="14" viewBox="0 0 14 14"><circle cx="7" cy="4.5" r="2.3" fill="var(--navy)"/><path d="M2.5 12.5c0-2.6 2-4.3 4.5-4.3s4.5 1.7 4.5 4.3z" fill="var(--navy)"/></svg></span>
    <span class="benefit__stem"></span>
    <p class="benefit__text">Licensed &amp; Certified Experts<br>Provide 100% Guarantee</p>
  </div>

  <div class="abs steps">
    <span><svg class="tick" viewBox="0 0 12 12"><circle cx="6" cy="6" r="6" fill="var(--navy)"/><path d="M3.3 6.1l1.8 1.8 3.6-3.6" stroke="#fff" stroke-width="1.4" fill="none"/></svg>SEND REFERRALS</span>
    <span><svg class="tick" viewBox="0 0 12 12"><circle cx="6" cy="6" r="6" fill="var(--navy)"/><path d="M3.3 6.1l1.8 1.8 3.6-3.6" stroke="#fff" stroke-width="1.4" fill="none"/></svg>GET PAID</span>
    <span><svg class="tick" viewBox="0 0 12 12"><circle cx="6" cy="6" r="6" fill="var(--navy)"/><path d="M3.3 6.1l1.8 1.8 3.6-3.6" stroke="#fff" stroke-width="1.4" fill="none"/></svg>GROW YOUR BUSINESS</span>
  </div>

  <div class="abs cta__label" style="left:29px;top:425px">CALL TEXT OR BOOK ON-LINE</div>
  <div class="abs cta__contact" style="left:290px;top:425px;font-size:13px">555-014-2796<i></i>TallowRidgeBuilders.example</div>

  <div class="abs badge" aria-label="24 hour emergency service">
    <span class="badge__num">24</span>
    <span class="badge__unit">HOUR</span>
  </div>
</section>

<section class="flyer flyer--back" aria-label="Referral program flyer back">
  <svg class="flyer__art" viewBox="0 0 719 465" xmlns="http://www.w3.org/2000/svg">
    <defs>
      <linearGradient id="panelTone" x1="0" y1="0" x2="1" y2="1">
        <stop offset="0" stop-color="#0d2f70"/>
        <stop offset="0.55" stop-color="#0b2456"/>
        <stop offset="1" stop-color="#0a1528"/>
      </linearGradient>
      <linearGradient id="moneyTone" x1="0" y1="0" x2="1" y2="1">
        <stop offset="0" stop-color="#e6e6df"/>
        <stop offset="0.5" stop-color="#b9bdb3"/>
        <stop offset="1" stop-color="#d3d5cc"/>
      </linearGradient>
      <linearGradient id="gold" x1="0" y1="0" x2="0" y2="1">
        <stop offset="0" stop-color="#fff200"/>
        <stop offset="1" stop-color="#f7931e"/>
      </linearGradient>
    </defs>
    <rect x="0" y="0" width="719" height="266" fill="url(#panelTone)"/>
    <polygon points="0,170 0,266 70,266" fill="#08142b" opacity=".6"/>
    <polygon points="264,0 719,0 719,266 300,266 222,99" fill="url(#moneyTone)" role="img" aria-label="Photo of hundred-dollar bills with letter tiles spelling CASH FLOW"/>

    <text class="hl-condensed" x="29" y="53" font-size="31" fill="#fff" textLength="166" lengthAdjust="spacingAndGlyphs">THE MORE YOU</text>
    <text class="hl-condensed" x="29" y="121" font-size="69" fill="url(#gold)" textLength="166" lengthAdjust="spacingAndGlyphs">REFER</text>
    <text class="hl-condensed" x="29" y="156" font-size="30" fill="#fff" textLength="166" lengthAdjust="spacingAndGlyphs">THE MORE YOU</text>
    <text class="hl-condensed" x="29" y="237" font-size="83" fill="url(#gold)" textLength="166" lengthAdjust="spacingAndGlyphs">EARN</text>

    <polygon points="0,423 324,423 330,436 324,450 0,450" fill="var(--red)"/>
    <polygon points="0,450 719,450 719,465 0,465" fill="var(--navy)"/>
  </svg>

  <h2 class="abs how">HOW IT WORKS</h2>
  <div class="abs how-rule"></div>

  <div class="step-photo" style="left:28px;background:linear-gradient(135deg,#d8d4cc,#6f98b8 60%,#3b6f96)" role="img" aria-label="Photo of drying fans on a wet floor"></div>
  <div class="step-copy" style="left:129px">
    <h3>REFER FLOOD, MOLD &amp;<br>CONSTRUCTION JOBS</h3>
    <p>It’s Simple to Refer 24/7:<br>Call, Text or Book Online.</p>
  </div>

  <div class="step-photo" style="left:258px;background:linear-gradient(160deg,#5f97cf,#b9d4ec 55%,#e9d35a)" role="img" aria-label="Photo of a yellow road sign reading Get Paid to Share against the sky"></div>
  <div class="step-copy" style="left:358px">
    <h3>WE TAKE CARE<br>OF EVERYTHING</h3>
    <p>We Schedule a Free<br>Estimate. If Approved,<br>You Get Paid.</p>
  </div>

  <div class="step-photo" style="left:477px;background:linear-gradient(135deg,#8db0d8,#dfe4e8 50%,#7f9a6a)" role="img" aria-label="Photo of an agent holding a listing sheet in front of a house"></div>
  <div class="step-copy" style="left:577px;width:125px">
    <h3>Everybody Benefits<br>From Referrals</h3>
    <p>We Provide Expert Quality<br>Work for Affordable Price</p>
  </div>

  <div class="abs refer-row">
    <span class="refer-row__pill">REFER</span>
    <span><svg class="tick" viewBox="0 0 12 12"><circle cx="6" cy="6" r="6" fill="var(--navy)"/><path d="M3.3 6.1l1.8 1.8 3.6-3.6" stroke="#fff" stroke-width="1.4" fill="none"/></svg>FLOODS</span>
    <i class="refer-row__sep"></i>
    <span><svg class="tick" viewBox="0 0 12 12"><circle cx="6" cy="6" r="6" fill="var(--navy)"/><path d="M3.3 6.1l1.8 1.8 3.6-3.6" stroke="#fff" stroke-width="1.4" fill="none"/></svg>REMODELS</span>
    <i class="refer-row__sep"></i>
    <span><svg class="tick" viewBox="0 0 12 12"><circle cx="6" cy="6" r="6" fill="var(--navy)"/><path d="M3.3 6.1l1.8 1.8 3.6-3.6" stroke="#fff" stroke-width="1.4" fill="none"/></svg>RENOVATIONS &amp; REPAIRS</span>
  </div>

  <div class="abs cta__label" style="left:29px;top:425px;font-size:16.5px">CALL TEXT OR BOOK ON-LINE</div>
  <div class="abs cta__contact" style="left:343px;top:424px;font-size:15px">555-014-2796<i></i>TallowRidgeBuilders.example</div>
</section>

</body>
</html>
```